KIVO 248
I need double sided standard sized Business Card [3.5" x 2"]
Open to designers choice
Modern
Pavel Rudakovsky
PO BOX 7132
Larkview, NV 90318
pavel@tumq4.com
kivo248.com

```html
<!DOCTYPE html>
<html lang="en">
<head>
<meta charset="utf-8">
<title>KIVO 248 – Business Card</title>
<link href="https://fonts.googleapis.com/css2?family=Open+Sans:wght@400;600;700&display=swap" rel="stylesheet">
<style>
  :root{
    --bg:#e9e7e4;
    --card:#ffffff;
    --orange:#f2552a;
    --ink:#5a5a5a;
    --soft:#9a9a9a;
    --grey:#4a4a4a;
  }
  *{box-sizing:border-box;margin:0;padding:0}
  html,body{width:1200px;height:629px;overflow:hidden;background:var(--bg);font-family:"Open Sans",Arial,sans-serif}
  .stage{position:relative;width:1200px;height:629px}
  .card{position:absolute;top:166px;width:520px;height:297px;background:var(--card);box-shadow:0 6px 18px rgba(0,0,0,.18);overflow:hidden}
  .card--front{left:50px}
  .card--back{left:630px}

  .brand{display:flex;align-items:center;gap:18px}
  .brand__mark{width:74px;height:74px;border-radius:14px;background:var(--grey)}
  .brand__name{font-weight:700;font-size:54px;color:var(--orange);letter-spacing:1px;line-height:1}
  .card--front .brand{position:absolute;left:110px;top:111px}

  .card--back .brand{position:absolute;left:44px;top:34px;gap:10px}
  .card--back .brand__mark{width:36px;height:36px;border-radius:7px}
  .card--back .brand__name{font-size:26px}

  .person{position:absolute;left:44px;top:150px;font-size:12px;color:var(--soft);line-height:1.45}
  .person__name{color:var(--orange);font-weight:600;font-size:13px}
  .person__role{margin-bottom:8px}

  .contacts{position:absolute;left:262px;top:118px;list-style:none;font-size:12px;color:var(--ink)}
  .contacts li{display:flex;align-items:center;gap:8px;height:21px}
  .contacts .dot{width:14px;height:14px;border-radius:50%;background:var(--orange);display:flex;align-items:center;justify-content:center}
  .contacts .dot svg{width:8px;height:8px}

  .footer-rule{position:absolute;left:0;right:0;bottom:22px;height:3px;background:var(--grey)}
  .footer-band{position:absolute;left:0;right:0;bottom:0;height:16px;background:var(--orange)}
</style>
</head>
<body>
<main class="stage">
  <section class="card card--front" aria-label="Card front">
    <div class="brand">
      <span class="brand__mark"></span>
      <span class="brand__name">KIVO 248</span>
    </div>
  </section>

  <section class="card card--back" aria-label="Card back">
    <div class="brand">
      <span class="brand__mark"></span>
      <span class="brand__name">KIVO 248</span>
    </div>

    <div class="person">
      <p class="person__name">Pavel Rudakovsky</p>
      <p class="person__role">CEO</p>
      <p>PO BOX 7132</p>
      <p>Larkview, NV 90318</p>
    </div>

    <ul class="contacts">
      <li><span class="dot"><svg viewBox="0 0 10 10"><path d="M2 1h2l1 2-1 1a5 5 0 0 0 2 2l1-1 2 1v2c-4 0-7-3-7-7z" fill="#fff"/></svg></span>555.201.4736</li>
      <li><span class="dot"><svg viewBox="0 0 10 10"><path d="M2 1h2l1 2-1 1a5 5 0 0 0 2 2l1-1 2 1v2c-4 0-7-3-7-7z" fill="#fff"/></svg></span>555.201.4737</li>
      <li><span class="dot"><svg viewBox="0 0 10 10"><rect x="1" y="3" width="8" height="5" fill="#fff"/></svg></span>555.201.4738</li>
      <li><span class="dot"><svg viewBox="0 0 10 10"><path d="M1 2h8v6H1z M1 2l4 3 4-3" fill="none" stroke="#fff"/></svg></span>pavel@tumq4.com</li>
      <li><span class="dot"><svg viewBox="0 0 10 10"><circle cx="5" cy="5" r="3.5" fill="none" stroke="#fff"/></svg></span>kivo248.com</li>
    </ul>

    <div class="footer-rule"></div>
    <div class="footer-band"></div>
  </section>
</main>
</body>
</html>
```